Signage Design Project

We need a logo and signage for the shopfront of a personal fitness training gym and coaching facility. We want the signage to cover the glass shopfront windows which consist of 4 glass windows with dimensions: 1 of 200cm x 180cm, 2 of 180cm x 135cm and 1 of 180cm x 180cm. The windows that are 200x 180 and 180x180 are the most visable/ important. We want the 200x180 to display the logo and our name which is "Harborline Fitness Centre" with further information of: Your personal training studio and boutique coaching gym Ph: 9471 2286.
For the window with 180 x 180cm measurement we want to list the services we provide which are:
Personal Training Sessions | Group Classes|Weight Loss |Toning & Sculpting|Bodybuilding I Cardio|Weights| Kettlebells| Boxing| Circuits I Team Building Programs| Boot Camp I Healthy Lifestyle & Wellness Coaching
The 2 windows 180x135cm are diagonal to the entry of the shop. We want them to be the same and plainer in design with the words: Harborline Fitness Centre
Personal Training Studio and Boutique Coaching Gym
The signage design also includes an acrylic window box that lights up which is to display the logo and Harborline Fitness Centre

```html
<!DOCTYPE html>
<html lang="en">
<head>
<meta charset="utf-8">
<title>Harborline Fitness Centre – Window Signage</title>
<link href="https://fonts.googleapis.com/css2?family=Nunito:wght@600;800;900&display=swap" rel="stylesheet">
<style>
  :root {
    --page: #efefef;
    --panel-deep: #b3200c;
    --panel-red: #d8320a;
    --panel-orange: #f0640c;
    --panel-amber: #ff9a12;
    --panel-yellow: #ffe21a;
    --ink-light: #ffffff;
    --ink-outline: #3a0a02;
  }
  * { box-sizing: border-box; margin: 0; padding: 0; }
  html, body {
    width: 1200px; height: 900px; overflow: hidden;
    background: var(--page);
    font-family: "Nunito", "Arial Rounded MT Bold", sans-serif;
  }
  .canvas { position: relative; width: 1200px; height: 900px; }

  .window-panel {
    position: absolute; top: 220px; height: 516px; overflow: hidden;
  }
  .window-panel--services { left: 36px; width: 588px; }
  .window-panel--identity { left: 650px; width: 514px; }

  .panel-backdrop {
    position: absolute; inset: 0;
    background:
      radial-gradient(circle at 78% 22%, var(--panel-yellow) 0, rgba(255,226,26,0) 18%),
      radial-gradient(circle at 20% 78%, var(--panel-amber) 0, rgba(255,154,18,0) 30%),
      radial-gradient(circle at 85% 80%, var(--panel-amber) 0, rgba(255,154,18,0) 26%),
      linear-gradient(135deg, var(--panel-red) 0%, var(--panel-orange) 45%, var(--panel-red) 75%, var(--panel-deep) 100%);
  }

  .outlined {
    color: var(--ink-light);
    font-weight: 900;
    text-shadow:
      -2px -2px 0 var(--ink-outline), 2px -2px 0 var(--ink-outline),
      -2px 2px 0 var(--ink-outline), 2px 2px 0 var(--ink-outline),
      0 -2px 0 var(--ink-outline), 0 2px 0 var(--ink-outline),
      -2px 0 0 var(--ink-outline), 2px 0 0 var(--ink-outline);
  }

  .service-list {
    position: absolute; left: 0; right: 0; top: 20px;
    list-style: none; text-align: center;
  }
  .service-list li { font-size: 24px; line-height: 30px; }
  .service-list .service--feature { font-size: 34px; line-height: 40px; }
  .service-list .service--headline { font-size: 38px; line-height: 46px; margin-top: 2px; }

  .brand-name {
    position: absolute; left: 40px; right: 20px; top: 72px;
    display: flex; align-items: center; gap: 18px;
    color: var(--ink-light); font-weight: 600;
    font-size: 50px; line-height: 54px;
  }
  .brand-name .brand-dot {
    flex: none; width: 56px; height: 56px; border-radius: 50%;
    background: var(--ink-light);
  }

  .tagline {
    position: absolute; left: 0; right: 0; top: 260px;
    text-align: center; font-size: 26px; line-height: 34px;
  }
  .phone {
    position: absolute; left: 0; right: 0; top: 440px;
    text-align: center; font-size: 28px;
  }
</style>
</head>
<body>
<main class="canvas">

  <section class="window-panel window-panel--services">
    <div class="panel-backdrop" role="img" aria-label="Glowing red, orange and yellow hexagon pattern background"></div>
    <ul class="service-list outlined">
      <li>Personal Training Sessions</li>
      <li class="service--feature" style="font-size:28px;line-height:32px">Group Classes</li>
      <li>Weight Loss</li>
      <li class="service--feature">Toning &amp; Sculpting</li>
      <li>Bodybuilding</li>
      <li>Cardio</li>
      <li>Weights</li>
      <li>Kettlebells</li>
      <li class="service--feature">Boxing</li>
      <li>Circuits</li>
      <li>Team Building Programs</li>
      <li class="service--headline">Boot Camp</li>
      <li>Healthy Lifestyle &amp; Wellness Coaching</li>
    </ul>
  </section>

  <section class="window-panel window-panel--identity">
    <div class="panel-backdrop" role="img" aria-label="Glowing red, orange and yellow hexagon pattern background"></div>
    <h1 class="brand-name"><span class="brand-dot"></span><span>Harborline<br>Fitness Centre</span></h1>
    <p class="tagline outlined">Your personal training studio<br>and<br>boutique coaching gym</p>
    <p class="phone outlined">Ph: 9471 2286</p>
  </section>

</main>
</body>
</html>
```